High end Sports Bar/ Restaurant Postcard Design

We are a high end sports bar/restaurant in forest hills on Benning street, we have high quality bar food, 24 draft beers, wine on tap and a great selection of whiskeys & scotches.
What we need is a brightly colored postcard that advertises our weekly events. It must be easy to read but eye-catching and full of fun images that will want to make people come in and drink & eat!
We are called Harlow Commons and have a gastropub feel with one entire wall covered in brick but with 9 t.v's all with audio for all sports games. We are definitely a restaurant too so its not all about sports however we will be carrying the GBX & Coastal Victory League Soccer packages.
On the back of the card we would like to advertise our lunch menu is Monday to Friday 10a.m - 3p.m. Dinner is Sunday - Monday 3p.m - 11p.m and Brunch on Saturday & Sunday. Late night bar menu also available Thursday, Friday & Saturday from 11p.m - 1a.m
Address: 54-16 Benning Street, Forest Hills, N.Y 11382 Phone number: 718 555.0143

Reason: We are extending the deadline to give us time to figure out which design is best for us, thank you all for your participation

Target Market(s)

21 - 45 year olds

Industry/Entity Type

Restaurant

Requirements
Must have
• Each individual days event must be eye-catching yet easy to read.

```html
<!DOCTYPE html>
<html lang="en">
<head>
<meta charset="utf-8">
<title>Harlow Commons – Weekly Events</title>
<link rel="stylesheet" href="https://fonts.googleapis.com/css2?family=Alfa+Slab+One&family=Fjalla+One&family=Yellowtail&display=swap">
<style>
  :root{
    --ink:#111111;
    --paper:#ffffff;
    --frame:#c9c9c9;
    --red:#ed1c24;
    --purple:#a96bb0;
    --lime:#6dbf58;
    --orange:#f7941d;
    --teal:#17b3c1;
    --green:#0aa24a;
    --violet:#6056a6;
    --slab:"Alfa Slab One", serif;
    --cond:"Fjalla One", sans-serif;
    --script:"Yellowtail", cursive;
  }
  html,body{margin:0;padding:0;overflow:hidden;background:var(--paper);}
  .card{position:relative;width:1200px;height:930px;background:var(--paper);overflow:hidden;
        box-sizing:border-box;border:2px solid var(--frame);border-radius:6px;}
  .block{position:absolute;box-sizing:border-box;}
  .side-strip{background:var(--ink);left:31px;width:83px;}
  .side-strip.top{top:31px;height:152px;}
  .side-strip.bottom{top:332px;height:566px;}
  .red-strip{background:var(--red);left:117px;width:92px;top:31px;height:867px;}

  .promo{top:31px;height:141px;text-align:center;color:var(--paper);}
  .promo .label{font-family:var(--slab);color:var(--ink);font-size:50px;line-height:1;margin-top:10px;letter-spacing:2px;}
  .promo .detail{font-family:var(--cond);font-size:52px;line-height:1;margin-top:10px;}
  .promo .detail small{font-size:28px;}
  .happy-hour{left:219px;width:558px;background:var(--purple);}
  .sunday{left:795px;width:315px;background:var(--lime);}

  .name-band{top:183px;left:31px;width:1150px;height:135px;background:var(--ink);color:var(--paper);}
  .venue-name{position:absolute;left:26px;top:26px;font-family:var(--slab);font-size:62px;line-height:1.2;margin:0;font-weight:400;}
  .venue-type{position:absolute;left:620px;top:18px;font-family:var(--cond);font-size:50px;line-height:1.05;}
  .weekly-events{position:absolute;left:970px;top:22px;font-family:var(--script);color:var(--red);
                 font-size:46px;line-height:.95;transform:rotate(-8deg);text-align:center;}

  .day{top:332px;width:182px;height:566px;text-align:center;color:var(--paper);font-family:var(--cond);}
  .day .day-name{font-family:var(--slab);color:var(--ink);font-size:50px;line-height:1;margin-top:10px;letter-spacing:1px;}
  .monday{left:219px;background:var(--orange);}
  .tuesday{left:414px;background:var(--teal);}
  .wednesday{left:606px;background:var(--green);}
  .thursday{left:798px;background:var(--violet);}
  .weekend{left:990px;width:180px;background:var(--red);}
  .weekend .day-name{font-size:44px;line-height:.9;}
  .weekend .day-name .and{display:block;font-size:24px;line-height:1.1;}

  .big{font-size:62px;line-height:1.18;}
  .mid{font-size:30px;line-height:1.3;}
  .small{font-size:24px;line-height:1.3;}
  .fine{font-size:20px;line-height:1.25;padding:0 8px;}
  .price{font-size:60px;line-height:1.1;margin-top:8px;}
  .deal{font-size:30px;line-height:1.45;margin-top:4px;}
  .gap{margin-top:26px;}
</style>
</head>
<body>
<main class="card">
  <div class="block side-strip top"></div>
  <div class="block side-strip bottom"></div>
  <div class="block red-strip"></div>

  <section class="block promo happy-hour">
    <div class="label">HAPPY HOUR</div>
    <div class="detail">Monday-Friday <small>11 a.m.</small></div>
  </section>
  <section class="block promo sunday">
    <div class="label">SUN</div>
    <div class="detail">Karaoke <small>9 p.m.</small></div>
  </section>

  <header class="block name-band">
    <h1 class="venue-name">Harlow Commons</h1>
    <div class="venue-type">Sports Bar<br>&amp; Restaurant</div>
    <div class="weekly-events">Weekly<br>Events</div>
  </header>

  <section class="block day monday">
    <div class="day-name">MON</div>
    <div class="price">$10</div>
    <div class="deal">BURGER + BEER<br>OR<br>SALAD + WINE</div>
    <div class="fine gap">*Choice of HC Burger, Garden Burger, or HC Chx Sandwich, Any Salad<br>*Chicken or Steak are additional</div>
  </section>

  <section class="block day tuesday">
    <div class="day-name">TUE</div>
    <div class="big">Happy<br>Hour<br>All Day<br>&amp;<br>Night</div>
  </section>

  <section class="block day wednesday">
    <div class="day-name">WED</div>
    <div class="big">Trivia<br>Night!</div>
    <div class="small gap">Come test your knowledge of irrelevant facts and win a prize!</div>
    <div class="mid gap">8 p.m.</div>
  </section>

  <section class="block day thursday">
    <div class="day-name">THU</div>
    <div class="big">Ladies<br>Night!</div>
    <div class="mid gap">8 p.m.-close</div>
    <div class="small gap">Ladies drink ½<br>price all night!</div>
  </section>

  <section class="block day weekend">
    <div class="day-name">FRI<span class="and">AND</span>SAT</div>
    <div class="big" style="font-size:50px;line-height:1.1;margin-top:6px">LIVE</div>
    <div class="small">Entertainment</div>
    <div class="mid gap" style="font-size:38px;line-height:1.2">Food &amp; Drink Specials Every Weekend</div>
  </section>
</main>
</body>
</html>
```